Aged Care Consultancy Business needs a business card design

I need a two sided business card - I want it clean and professional. Surprise me

Target Market(s)

middle aged and ageing victorians

Industry/Entity Type

Health Care

Contact Information for Business Card

Text to be included

Logo
Aged Care Consulting Services
Professional, Reliable, Affordable

Tovan Brelsick
Director
0427 31 64 92 (larger)
1300 73 29 41
tovan@wadolire.com.au
www.wadolcare.com.au
Facebook (details TBA)

include little icons beside the contact info:

- Envelope = email
- Phone = phone
- Globe = website

Font styles to use
Serif
Sans Serif

Requirements
Must have
• look proffesional and clean

```html
<!DOCTYPE html>
<html lang="en">
<head>
<meta charset="utf-8">
<title>Wadol Care – Business Card</title>
<link href="https://fonts.googleapis.com/css2?family=Arimo:wght@400;700&display=swap" rel="stylesheet">
<style>
  :root {
    --bg: #2b2b2d;
    --orange: #f09a0c;
    --orange-deep: #e48a06;
    --blue: #0f4a8a;
    --blue-dark: #0b3a70;
    --white: #ffffff;
    --ink: #4a4a4a;
    --rule: #f0a020;
  }
  * { box-sizing: border-box; margin: 0; padding: 0; }
  html, body {
    width: 1200px; height: 843px; overflow: hidden;
    background: var(--bg);
    font-family: "Arimo", Arial, sans-serif;
  }
  .canvas {
    position: relative; width: 1200px; height: 843px;
    display: flex; align-items: center; justify-content: center; gap: 40px;
  }
  .card {
    position: relative; width: 540px; height: 330px; overflow: hidden;
    box-shadow: 0 12px 30px rgba(0,0,0,.45);
  }

  /* Back side */
  .card--back {
    background: linear-gradient(135deg, var(--orange) 0%, var(--orange-deep) 100%);
    color: var(--white);
  }
  .back-brand {
    position: absolute; left: 0; right: 0; top: 118px;
    text-align: center; font-weight: 700; font-size: 50px; letter-spacing: 1px;
  }
  .back-service, .back-values {
    position: absolute; bottom: 26px; font-size: 13px; letter-spacing: .4px;
  }
  .back-service { left: 28px; }
  .back-values { right: 28px; }

  /* Front side */
  .card--front { background: var(--white); }
  .front-band { position: absolute; inset: 0; width: 540px; height: 330px; }
  .front-brand {
    position: absolute; right: 36px; top: 108px;
    display: flex; align-items: center; gap: 10px;
    font-weight: 700; font-size: 40px; color: var(--blue);
  }
  .front-brand .dot {
    width: 18px; height: 18px; border-radius: 50%; background: var(--orange);
  }
  .person { position: absolute; left: 32px; top: 120px; }
  .person-name { font-weight: 700; font-size: 19px; color: var(--blue); }
  .person-role { font-size: 14px; color: var(--orange); margin-top: 2px; }
  .contacts {
    position: absolute; left: 32px; top: 186px; list-style: none;
    font-size: 14px; color: var(--ink);
  }
  .contacts li { display: flex; align-items: center; gap: 9px; height: 22px; }
  .contacts .phone-main { font-size: 15px; }
  .icon { width: 14px; height: 14px; flex: none; fill: var(--blue); }
  .divider {
    position: absolute; left: 262px; top: 196px; width: 2px; height: 82px;
    background: var(--rule);
  }
  .online { left: 282px; top: 230px; }
  .square { width: 13px; height: 13px; background: var(--blue); flex: none; }
</style>
</head>
<body>
<main class="canvas">

  <section class="card card--back" aria-label="Card back">
    <div class="back-brand">wadol care</div>
    <p class="back-service">Aged Care Consulting Services</p>
    <p class="back-values">Professional, Reliable, Affordable</p>
  </section>

  <section class="card card--front" aria-label="Card front">
    <svg class="front-band" viewBox="0 0 540 330" aria-hidden="true">
      <path d="M0 0 H380 C250 10 120 40 0 110 Z" fill="var(--blue)"/>
      <path d="M0 110 C120 40 250 10 380 0 H410 C270 15 130 50 0 128 Z" fill="var(--blue-dark)" opacity=".35"/>
    </svg>

    <div class="front-brand"><span class="dot"></span>wadol care</div>

    <div class="person">
      <h1 class="person-name">Tovan Brelsick</h1>
      <p class="person-role">Director</p>
    </div>

    <ul class="contacts">
      <li class="phone-main">
        <svg class="icon" viewBox="0 0 24 24"><path d="M6.6 10.8a15 15 0 0 0 6.6 6.6l2.2-2.2a1 1 0 0 1 1-.25 11.4 11.4 0 0 0 3.6.57 1 1 0 0 1 1 1V20a1 1 0 0 1-1 1A17 17 0 0 1 3 4a1 1 0 0 1 1-1h3.5a1 1 0 0 1 1 1 11.4 11.4 0 0 0 .57 3.6 1 1 0 0 1-.25 1z"/></svg>
        0427 31 64 92
      </li>
      <li>
        <svg class="icon" viewBox="0 0 24 24"><path d="M6.6 10.8a15 15 0 0 0 6.6 6.6l2.2-2.2a1 1 0 0 1 1-.25 11.4 11.4 0 0 0 3.6.57 1 1 0 0 1 1 1V20a1 1 0 0 1-1 1A17 17 0 0 1 3 4a1 1 0 0 1 1-1h3.5a1 1 0 0 1 1 1 11.4 11.4 0 0 0 .57 3.6 1 1 0 0 1-.25 1z"/></svg>
        1300 73 29 41
      </li>
      <li>
        <svg class="icon" viewBox="0 0 24 24"><path d="M2 5h20v14H2z M2 5l10 8 10-8" fill="var(--blue)" stroke="var(--white)" stroke-width="1.5"/></svg>
        tovan@wadolire.com.au
      </li>
    </ul>

    <div class="divider"></div>

    <ul class="contacts online">
      <li>
        <svg class="icon" viewBox="0 0 24 24"><circle cx="12" cy="12" r="10"/><path d="M2 12h20M12 2c3 3 3 17 0 20M12 2c-3 3-3 17 0 20" stroke="var(--white)" stroke-width="1.4" fill="none"/></svg>
        www.wadolcare.com.au
      </li>
      <li><span class="square"></span>wadolcare</li>
    </ul>
  </section>

</main>
</body>
</html>
```